Women's Online Clothing Boutique Needs Business Cards

I already have a logo that I would like to use. Some of the things that interest me is black business cards, foil embossed logo, glossy embossed logo, leopard print, no yellow font, rounded edges. I even like just a large logo on the front side with all of my information on the back side.

Contact Information for Business Card

https://copperfinch.shopvendly.example/
https://www.facebook.com/thecopperfinchboutique/
https://www.instagram.com/thecopperfinchboutique/
copperfinchboutique@mailora.example

Requirements
Must have
• My Logo
Nice to have
• Leopard Print
Should not have
• No Yellow Font

```html
<!DOCTYPE html>
<html lang="en">
<head>
<meta charset="utf-8">
<title>The Copper Finch Boutique – Business Cards</title>
<link rel="stylesheet" href="https://fonts.googleapis.com/css2?family=Montserrat:wght@400&display=swap">
<style>
  :root {
    --stage: #2a211b;
    --card: #0d0d0e;
    --card-sheen: #3a3a3d;
    --gold: #c9a04a;
    --gold-soft: rgba(201, 160, 74, 0.6);
  }
  * { box-sizing: border-box; margin: 0; padding: 0; }
  html, body {
    width: 1200px;
    height: 913px;
    overflow: hidden;
    background: var(--stage);
    font-family: "Montserrat", Arial, sans-serif;
  }
  .stage {
    position: relative;
    width: 1200px;
    height: 913px;
  }
  .card {
    position: absolute;
    width: 600px;
    height: 343px;
    border-radius: 26px;
    border: 1.5px solid var(--gold);
    background: linear-gradient(150deg, var(--card-sheen) 0%, var(--card) 55%, #050506 100%);
    color: var(--gold);
    box-shadow: 0 0 0 4px var(--card), 0 0 0 5.5px var(--gold);
  }
  .card--front { left: 60px; top: 80px; }
  .card--back  { left: 540px; top: 490px; }

  .wordmark {
    position: absolute;
    left: 50%;
    transform: translateX(-50%);
    display: flex;
    align-items: center;
    gap: 12px;
    white-space: nowrap;
    font-weight: 400;
    color: var(--gold);
  }
  .wordmark__dot {
    border-radius: 50%;
    background: var(--gold);
    flex: none;
  }
  .card--front .wordmark { top: 136px; font-size: 32px; line-height: 40px; }
  .card--front .wordmark__dot { width: 18px; height: 18px; }
  .card--back .wordmark { top: 38px; font-size: 21px; line-height: 28px; gap: 9px; }
  .card--back .wordmark__dot { width: 12px; height: 12px; }

  .rule {
    position: absolute;
    height: 1px;
    background: var(--gold-soft);
  }
  .card--front .rule--top    { left: 150px; right: 90px; top: 120px; }
  .card--front .rule--bottom { left: 90px; right: 150px; top: 194px; }
  .card--back .rule--top     { left: 170px; right: 110px; top: 30px; }
  .card--back .rule--bottom  { left: 110px; right: 170px; top: 76px; }

  .contact-icons {
    position: absolute;
    top: 98px;
    left: 50%;
    transform: translateX(-50%);
    display: flex;
    gap: 8px;
  }
  .contact-icons svg { width: 24px; height: 24px; display: block; }

  .contact-list {
    position: absolute;
    top: 150px;
    left: 20px;
    right: 20px;
    list-style: none;
    text-align: center;
    font-size: 15px;
    line-height: 30px;
    letter-spacing: 0.2px;
    white-space: nowrap;
  }
  .card--back .rule--list { left: 60px; right: 60px; top: 140px; }
</style>
</head>
<body>
<main class="stage">

  <section class="card card--front" aria-label="Business card front">
    <span class="rule rule--top"></span>
    <div class="wordmark">
      <span class="wordmark__dot"></span>
      <span class="wordmark__name">The Copper Finch Boutique</span>
    </div>
    <span class="rule rule--bottom"></span>
  </section>

  <section class="card card--back" aria-label="Business card back">
    <span class="rule rule--top"></span>
    <div class="wordmark">
      <span class="wordmark__dot"></span>
      <span class="wordmark__name">The Copper Finch Boutique</span>
    </div>
    <span class="rule rule--bottom"></span>

    <div class="contact-icons">
      <svg viewBox="0 0 24 24" aria-label="Email">
        <circle cx="12" cy="12" r="11" fill="var(--gold)"/>
        <rect x="6" y="8" width="12" height="8" fill="none" stroke="#0d0d0e" stroke-width="1.4"/>
        <path d="M6 8l6 5 6-5" fill="none" stroke="#0d0d0e" stroke-width="1.4"/>
      </svg>
      <svg viewBox="0 0 24 24" aria-label="Website">
        <circle cx="12" cy="12" r="11" fill="var(--gold)"/>
        <circle cx="12" cy="12" r="6" fill="none" stroke="#0d0d0e" stroke-width="1.3"/>
        <ellipse cx="12" cy="12" rx="2.6" ry="6" fill="none" stroke="#0d0d0e" stroke-width="1.2"/>
        <path d="M6 12h12" stroke="#0d0d0e" stroke-width="1.2"/>
      </svg>
      <svg viewBox="0 0 24 24" aria-label="Social page">
        <circle cx="12" cy="12" r="11" fill="var(--gold)"/>
      </svg>
      <svg viewBox="0 0 24 24" aria-label="Social profile">
        <circle cx="12" cy="12" r="11" fill="var(--gold)"/>
      </svg>
    </div>

    <span class="rule rule--list"></span>
    <ul class="contact-list">
      <li>copperfinchboutique@mailora.example</li>
      <li>https://copperfinch.shopvendly.example/</li>
      <li>https://www.friendloop.example/thecopperfinchboutique/</li>
      <li>https://www.snapgrid.example/thecopperfinchboutique/</li>
    </ul>
  </section>

</main>
</body>
</html>
```